Breezeway Climate Business Card Design

Design new, 2 sides, business cards for a residential and light commercial heating, air conditioning contractor.

Target Market(s)

Homeowners, small businesses

Industry/Entity Type

Business

Contact Information for Business Card

Dominic Vasquerelli
Phone - 555-214-6837
Email
Address - PO box 618
Millbrook NJ 07999
Website - www.BreezewayClimateLLC.example

Requirements
Must have
• logo, company colors, standard size with no die cut, so I can use printhaven

```html
<!DOCTYPE html>
<html lang="en">
<head>
<meta charset="utf-8">
<title>Breezeway Climate Business Card</title>
<link href="https://fonts.googleapis.com/css2?family=Open+Sans:wght@300;400;600;700&display=swap" rel="stylesheet">
<style>
  :root {
    --bg: #2a2c30;
    --card-red: #a3222f;
    --card-red-dark: #8e1b27;
    --accent-orange: #f39322;
    --text-light: #fbeee6;
    --text-muted: #e6b9b9;
  }
  * { margin: 0; padding: 0; box-sizing: border-box; }
  html, body {
    width: 1200px; height: 900px; overflow: hidden;
    background: var(--bg);
    font-family: "Open Sans", Arial, sans-serif;
  }
  .stage {
    width: 1200px; height: 900px;
    display: flex; flex-direction: column;
    align-items: center; justify-content: center; gap: 60px;
  }
  .card {
    position: relative;
    width: 560px; height: 320px;
    border-radius: 26px;
    background: var(--card-red);
    overflow: hidden;
    color: var(--text-light);
  }
  /* logo side */
  .brand-mark {
    position: absolute; inset: 0;
    display: flex; align-items: center; justify-content: center; gap: 14px;
  }
  .brand-dot {
    width: 22px; height: 22px; border-radius: 50%;
    background: var(--accent-orange);
  }
  .brand-name {
    font-weight: 700; font-size: 36px; color: var(--accent-orange);
    letter-spacing: 0.5px;
  }
  /* info side */
  .edge-lines {
    position: absolute; display: flex; gap: 6px;
  }
  .edge-lines span { display: block; width: 5px; height: 100%; background: var(--accent-orange); }
  .edge-lines--top { left: 26px; top: 0; height: 148px; }
  .edge-lines--bottom { right: 26px; bottom: 0; height: 64px; }
  .holder {
    position: absolute; left: 62px; top: 40px;
  }
  .holder-name {
    font-weight: 700; font-size: 25px; letter-spacing: 1px; text-transform: uppercase;
  }
  .holder-title {
    font-weight: 300; font-size: 14px; color: var(--text-muted); margin-top: 2px;
  }
  .contact-list {
    position: absolute; left: 28px; top: 182px;
    list-style: none; font-size: 13px; line-height: 1.45;
  }
  .contact-list li { display: flex; gap: 10px; align-items: flex-start; margin-bottom: 4px; }
  .contact-list svg { flex: none; width: 13px; height: 13px; margin-top: 3px; }
  .info-brand {
    position: absolute; right: 90px; top: 150px;
    display: flex; align-items: center; gap: 8px;
  }
  .info-brand .brand-dot { width: 14px; height: 14px; }
  .info-brand .brand-name { font-size: 22px; }
  .website {
    position: absolute; right: 70px; bottom: 22px;
    display: flex; align-items: center; gap: 8px; font-size: 14px;
  }
  .website svg { width: 15px; height: 15px; }
</style>
</head>
<body>
<main class="stage">
  <section class="card card--logo" aria-label="Card back">
    <div class="brand-mark">
      <span class="brand-dot"></span>
      <span class="brand-name">Breezeway Climate</span>
    </div>
  </section>

  <section class="card card--info" aria-label="Card front">
    <div class="edge-lines edge-lines--top"><span></span><span></span></div>
    <div class="holder">
      <h1 class="holder-name">Dominic Vasquerelli</h1>
      <p class="holder-title">CEO &amp; Founder</p>
    </div>
    <ul class="contact-list">
      <li>
        <svg viewBox="0 0 16 16" fill="none" stroke="currentColor" stroke-width="1.4"><path d="M4 1.5l2.5 3-1.5 1.5a8 8 0 0 0 5 5l1.5-1.5 3 2.5-1.5 2.5C7 14 2 9 1.5 3z"/></svg>
        <span>555-214-6837</span>
      </li>
      <li>
        <svg viewBox="0 0 16 16" fill="none" stroke="currentColor" stroke-width="1.4"><rect x="1.5" y="3.5" width="13" height="9"/><path d="M1.5 3.5l6.5 5 6.5-5"/></svg>
        <span>info@breezewayclimate.example</span>
      </li>
      <li>
        <svg viewBox="0 0 16 16" fill="none" stroke="currentColor" stroke-width="1.4"><path d="M8 15s5-5 5-9a5 5 0 0 0-10 0c0 4 5 9 5 9z"/><circle cx="8" cy="6" r="1.8"/></svg>
        <span>PO box 618,<br>Millbrook NJ 07999</span>
      </li>
    </ul>
    <div class="info-brand">
      <span class="brand-dot"></span>
      <span class="brand-name">Breezeway Climate</span>
    </div>
    <div class="website">
      <span>www.BreezewayClimateLLC.example</span>
      <svg viewBox="0 0 16 16" fill="none" stroke="currentColor" stroke-width="1.2"><circle cx="8" cy="8" r="6.5"/><ellipse cx="8" cy="8" rx="3" ry="6.5"/><path d="M1.5 8h13M2.5 4.8h11M2.5 11.2h11"/></svg>
    </div>
    <div class="edge-lines edge-lines--bottom"><span></span><span></span></div>
  </section>
</main>
</body>
</html>
```